Software development and consultancy website

Company – Velmoria Limited , London, UK
Profile – we are providing integration solutions development / consultancy services for QOR integration projects across UK.
Our name refers two words - integration and grace - and it shows our clients our main specialization field and key characteristics of our solutions / products. We also would like to be associated with follow words: smart, reliable, unique.
The target audience is experienced IT professionals and managers.
Website look and feel should be professional and sophisticated, simple and elegant. I like minimalistic themes with no real object/people photos. Try to avoid messy/cluttered/colourful content. White dominating background is a must, don’t like dark websites.
I would prefer light, web 2.0 style colours, follow are in my main interest:
- combination of light grey and orange
- Logo colours
In terms of deliverables, theme should be coded and be ready to be placed to my test website. I would also suggest if you could create skin for Tundle theme. NOTE: Please make a quote excluding Tundle theme cost.
Attached are examples of logo and corporate stationery design and mockups of website with landing page layout and content page layout. Website design should not copy stationery design but to be consistent with.
Sites I like :
http://www.brelwickpost.com/
http://www.vantrel.com/
http://www.holmfarq.com/quillscope/
http://www.dorvique.com/
I changed project type to Context and increased the budget. Please refer project description for details
It Company

```html
<!DOCTYPE html>
<html lang="en">
<head>
<meta charset="utf-8">
<title>Velmoria Limited</title>
<link rel="stylesheet" href="https://fonts.googleapis.com/css2?family=Source+Sans+3:wght@400;600;700&display=swap">
<style>
:root{
  --ink:#333;
  --grey:#666;
  --orange:#f08a12;
  --orange-light:#ffb640;
  --green:#8cb61a;
  --green-text:#7ab317;
  --blue:#2a9fd6;
  --blue-text:#1d8ec8;
  --slide-top:#19b6f2;
  --slide-bottom:#0b9ddc;
  --navy:#15314d;
  --footer:#1c1c1c;
  --footer-text:#e6e6e6;
}
*{margin:0;padding:0;box-sizing:border-box}
html,body{width:817px;height:1200px;overflow:hidden;background:#fff}
body{position:relative;font-family:"Source Sans 3",sans-serif;color:var(--ink)}
.abs{position:absolute}
.logo{left:22px;top:28px;display:flex;align-items:center;gap:8px}
.logo-dot{width:36px;height:36px;border-radius:50%;background:var(--orange)}
.logo-name{font-size:40px;font-weight:600;color:#555;line-height:1}
.nav a{position:absolute;top:38px;font-size:11px;color:var(--grey);text-decoration:none}
.nav .current{left:398px;top:35px;width:58px;height:22px;border-radius:11px;background:linear-gradient(var(--orange-light),var(--orange));color:#fff;text-align:center;line-height:22px;border:1px solid #e07a00}
.slider{left:22px;top:93px;width:542px;height:250px;background:#fff;box-shadow:0 1px 4px rgba(0,0,0,.25)}
.slide{position:absolute;left:5px;top:4px;width:531px;height:240px;background:linear-gradient(var(--slide-top),var(--slide-bottom))}
.slide-preview{left:46px;top:33px;width:228px;height:163px;background:linear-gradient(#dfe6ea,#c7d0d6);border-radius:3px}
.slide-title{left:306px;top:47px;font-size:19px;font-weight:700;color:var(--navy)}
.slide-list{left:306px;top:77px;list-style:none;color:#fff;font-size:11px;font-weight:600;line-height:17.7px}
.slide-mascot{left:428px;top:143px;width:78px;height:82px;border-radius:50%;background:radial-gradient(circle at 40% 35%,#4fb6ff,#0a4fc4)}
.pager{left:223px;top:221px;width:97px;height:19px;background:#fff;border-radius:3px 3px 0 0;display:flex;gap:6px;justify-content:center;align-items:center}
.pager span{width:8px;height:8px;border-radius:50%;background:#1a6fa8}
.pager span.on{background:#cfd8de}
.arrow{top:198px}
.slider-shadow{left:60px;top:340px;width:470px;height:24px;border-radius:50%;background:radial-gradient(rgba(0,0,0,.25),transparent 70%)}
.feature-title{left:596px;top:116px;font-size:19px;color:#555;line-height:23px;font-weight:400}
.feature{left:593px;width:200px}
.feature-icon{position:absolute;left:0;top:0;width:36px;height:34px;border-radius:4px}
.feature p{position:absolute;left:48px;top:-3px;width:152px;font-size:10px;line-height:12.5px}
.more{position:absolute;width:38px;height:15px;border-radius:8px;font-size:9px;color:#222;text-align:center;line-height:15px}
.dashes{left:586px;width:206px;border-top:2px dashed #ccc}
.band{left:0;top:397px;width:817px;height:298px;background:linear-gradient(#e6e6e6,#fafafa 40%,#f4f4f4 85%,#e2e2e2)}
.h2{font-size:22px;line-height:1;font-weight:400}
.green{color:var(--green)}
.blue{color:var(--blue)}
.hl{color:#e57c10}
.about p{position:absolute;left:65px;width:340px;font-size:13px;line-height:16px;color:#333}
.support-intro{left:498px;top:454px;font-size:12.5px;line-height:16px;color:#333}
.form label{position:absolute;left:498px;font-size:10.5px;color:#444}
.form .colon{position:absolute;left:586px;font-size:10.5px}
.field{position:absolute;left:598px;width:195px;background:#fff;border:1px solid #888}
.btn{position:absolute;border-radius:11px;background:linear-gradient(var(--orange-light),var(--orange));color:#222;text-align:center;border:1px solid #e07a00}
.post .avatar{position:absolute;width:58px;height:68px;border-radius:50% 50% 8px 8px;background:linear-gradient(#8a8a8a,#3c3c3c)}
.post .date{position:absolute;font-size:11px}
.post p{position:absolute;width:230px;font-size:11.3px;line-height:14px}
.readmore{position:absolute;font-size:11px;color:var(--orange)}
.divider{left:404px;top:738px;width:1px;height:318px;background:#ccc}
.subscribe{left:427px;top:928px;width:369px;height:109px;background:#ebebeb;border-radius:8px}
.footer{left:0;top:1076px;width:817px;height:124px;background:linear-gradient(#2a2a2a,var(--footer));color:var(--footer-text);font-size:9px;line-height:12px}
.vsep{position:absolute;top:16px;width:1px;height:90px;background:#444}
.social{position:absolute;width:28px;height:28px;border-radius:50%}
</style>
</head>
<body>

<header>
  <div class="abs logo"><span class="logo-dot"></span><span class="logo-name">velmoria</span></div>
  <nav class="nav">
    <a class="current" href="#">Home</a>
    <a href="#" style="left:471px">About Us</a>
    <a href="#" style="left:559px">Products</a>
    <a href="#" style="left:647px">Services</a>
    <a href="#" style="left:736px">Blog</a>
  </nav>
</header>

<section class="abs slider">
  <div class="slide">
    <div class="abs slide-preview" role="img" aria-label="Preview of an under-construction page template with a download button"></div>
    <div class="abs slide-title">Features</div>
    <ul class="abs slide-list">
      <li>- Fully Customizable</li>
      <li>- Easy to modify &amp; Change colors</li>
      <li>- Well organized .psd files</li>
      <li>- Grouped Layers</li>
      <li>- Labelled Layers</li>
    </ul>
    <div class="abs slide-mascot" role="img" aria-label="Blue round mascot"></div>
    <div class="abs pager"><span></span><span></span><span class="on"></span><span></span><span></span></div>
  </div>
</section>
<svg class="abs arrow" style="left:16px" width="30" height="44" viewBox="0 0 30 44"><path d="M24 4 L8 22 L24 40" fill="none" stroke="#555" stroke-width="7" stroke-linecap="round" stroke-linejoin="round"/></svg>
<svg class="abs arrow" style="left:542px" width="30" height="44" viewBox="0 0 30 44"><path d="M6 4 L22 22 L6 40" fill="none" stroke="#555" stroke-width="7" stroke-linecap="round" stroke-linejoin="round"/></svg>
<div class="abs slider-shadow"></div>

<aside>
  <h2 class="abs feature-title">How to make a Perfect<br>QOR PI Project</h2>
  <div class="abs feature" style="top:180px">
    <div class="feature-icon" role="img" aria-label="Settings folder icon" style="background:linear-gradient(#f7c04a,#d98a10)"></div>
    <p style="color:var(--green-text)">Lorem Ipsum is that it has a more-or-<br>less normal distribution</p>
    <span class="more" style="left:155px;top:22px;background:linear-gradient(#b6e24a,#7bb816)">more..</span>
  </div>
  <div class="abs dashes" style="top:228px"></div>
  <div class="abs feature" style="top:240px">
    <div class="feature-icon" role="img" aria-label="Notepad and pencil icon" style="background:linear-gradient(#fafafa,#cfcfcf)"></div>
    <p style="left:51px;color:var(--blue-text)">Lorem Ipsum is that it has a more-or-<br>less normal</p>
    <span class="more" style="left:157px;top:21px;background:linear-gradient(#9ad8ff,#3ca6e6)">more..</span>
  </div>
  <div class="abs dashes" style="top:289px"></div>
  <div class="abs feature" style="top:302px">
    <div class="feature-icon" role="img" aria-label="Parcel box icon" style="background:linear-gradient(#e8c27a,#b88a3c)"></div>
    <p style="color:var(--orange)">Lorem Ipsum is that it has a more-or-<br>less normal</p>
    <span class="more" style="left:156px;top:20px;background:linear-gradient(var(--orange-light),var(--orange))">more..</span>
  </div>
</aside>

<div class="abs band"></div>

<section class="about">
  <div class="abs" role="img" aria-label="Businessman icon" style="left:25px;top:408px;width:28px;height:40px;border-radius:4px;background:linear-gradient(#6b7a8a,#1e2a36)"></div>
  <h2 class="abs h2 green" style="left:62px;top:424px">Who We Are ?</h2>
  <p style="top:470px">Contrary to popular belief, Lorem Ipsum is not simply random text. It has roots in a piece of classical Latin literature from 45 BC, making it over 2000 years old. <span class="hl">Edwin Harrowgate</span></p>
  <p style="top:533px">Contrary to popular belief, Lorem Ipsum is not simply random text. <span class="hl">It has roots in a piece of classical</span> Latin literature from 45 BC, making it over 2000 years old. Edwin Harrowgate</p>
  <p style="top:597px">Contrary to popular belief, Lorem Ipsum is not simply random text. It has roots in a piece of classical Latin literature from 45 BC, making it over 2000 years old. <span class="hl">Edwin Harrowgate</span></p>
</section>

<section class="support form">
  <svg class="abs" style="left:446px;top:415px" width="40" height="40" viewBox="0 0 40 40"><circle cx="20" cy="20" r="15" fill="none" stroke="#e5502a" stroke-width="8"/><circle cx="20" cy="20" r="15" fill="none" stroke="#fff" stroke-width="8" stroke-dasharray="11.8 11.8" stroke-dashoffset="6"/><circle cx="20" cy="20" r="19" fill="none" stroke="#aaa" stroke-width="1"/></svg>
  <h2 class="abs h2 green" style="left:494px;top:422px">Support</h2>
  <p class="abs support-intro">Have a look on our help section or<br>Raise a new ticket right now !</p>
  <div class="abs" role="img" aria-label="Support ticket illustration" style="left:742px;top:437px;width:50px;height:42px;background:linear-gradient(135deg,#ffd04a,#e89a10);border-radius:4px;transform:rotate(-20deg)"></div>
  <label style="top:499px">Your name</label><span class="colon" style="top:499px">:</span><div class="field" style="top:497px;height:19px"></div>
  <label style="top:524px">Your Email</label><span class="colon" style="top:524px">:</span><div class="field" style="top:521px;height:19px"></div>
  <label style="top:550px">Your Question</label><span class="colon" style="top:550px">:</span><div class="field" style="top:546px;height:67px"></div>
  <label style="top:626px">Captcha</label><span class="colon" style="top:626px">:</span>
  <div class="abs" role="img" aria-label="Captcha challenge image" style="left:598px;top:622px;width:122px;height:48px;background:linear-gradient(#f4f4f4,#dadada);border:1px solid #bbb"></div>
  <span class="btn" style="left:727px;top:641px;width:78px;height:22px;font-size:14px;line-height:20px">Submit</span>
</section>

<section class="blog">
  <div class="abs" role="img" aria-label="Blue speech bubble icon" style="left:22px;top:708px;width:54px;height:50px;border-radius:50%;background:radial-gradient(circle at 40% 35%,#6fcfff,#0b6fbf)"></div>
  <h2 class="abs h2 blue" style="left:91px;top:721px">Recent Blog</h2>
  <div class="post">
    <div class="avatar" role="img" aria-label="Author silhouette" style="left:65px;top:775px"></div>
    <span class="date" style="left:136px;top:787px">25/12/2011</span>
    <p style="left:136px;top:806px">Lorem Ipsum is simply dummy text of the print-<br>ing and typesetting industry. Lorem Ipsum has<br>been the industry's</p>
    <span class="readmore" style="left:298px;top:862px">readmore...</span>
  </div>
  <div class="post">
    <div class="avatar" role="img" aria-label="Author silhouette" style="left:62px;top:890px"></div>
    <span class="date" style="left:132px;top:898px">25/12/2011</span>
    <p style="left:132px;top:917px">Lorem Ipsum is simply dummy text of the print-<br>ing and typesetting industry. Lorem Ipsum has<br>been the industry's</p>
    <span class="readmore" style="left:294px;top:973px">readmore...</span>
  </div>
</section>

<div class="abs divider"></div>

<section class="news">
  <div class="abs" role="img" aria-label="Newspaper icon" style="left:445px;top:715px;width:52px;height:50px;border-radius:4px;background:linear-gradient(#f2f2f2,#bdbdbd)"></div>
  <h2 class="abs h2 blue" style="left:508px;top:722px">Latest News</h2>
  <div class="post">
    <span class="date" style="left:514px;top:774px">25/12/2011</span>
    <div class="abs" role="img" aria-label="Small newspaper icon" style="left:578px;top:773px;width:18px;height:16px;background:#ddd;border-radius:2px"></div>
    <p style="left:514px;top:793px">Lorem Ipsum is simply dummy text of the print-<br>ing and typesetting industry.</p>
    <span class="readmore" style="left:675px;top:821px">readmore...</span>
  </div>
  <div class="abs" style="left:508px;top:841px;width:252px;border-top:2px dashed #ccc"></div>
  <div class="post">
    <span class="date" style="left:514px;top:852px">25/12/2011</span>
    <div class="abs" role="img" aria-label="Small newspaper icon" style="left:578px;top:851px;width:18px;height:16px;background:#ddd;border-radius:2px"></div>
    <p style="left:514px;top:871px">Lorem Ipsum is simply dummy text of the print-<br>ing and typesetting industry.</p>
    <span class="readmore" style="left:675px;top:899px">readmore...</span>
  </div>
  <div class="abs" style="left:508px;top:917px;width:252px;border-top:2px dashed #ccc"></div>

  <div class="abs subscribe">
    <span class="abs" style="left:46px;top:4px;font-size:14px;color:var(--blue)">Subscribe on our monthly</span>
    <span class="abs" style="left:46px;top:27px;font-size:14px;color:var(--orange)">News Letter :</span>
    <div class="abs" style="left:131px;top:27px;width:195px;height:19px;background:#fff;border:1px solid #777"></div>
    <span class="btn" style="left:264px;top:51px;width:62px;height:18px;font-size:11.5px;line-height:16px">Submit</span>
    <span class="abs" style="left:39px;top:76px;font-size:9.5px;line-height:12.5px">yes, only 1 full-of-goodies email per month. Honestly!<br>And we hate spammers so we will not give out your email to anyone.</span>
  </div>
</section>

<footer class="abs footer">
  <div class="abs" style="left:23px;top:24px">Velmoria Limited<br>Registered address : 48 Larkspur House,<br><span style="padding-left:83px">210 Quillon Road,</span><br><span style="padding-left:83px">London, SE4 7PD, United Kingdom</span></div>
  <div class="abs" style="left:23px;top:83px">Company Registration No :<br><span style="padding-left:78px">784215 (England and Wales)</span></div>
  <span class="vsep" style="left:269px"></span>
  <div class="abs" style="left:280px;top:18px;width:296px;text-align:center">Website Disclaimer &nbsp;|&nbsp; Terms and Conditions &nbsp;|&nbsp; Privacy Policy</div>
  <div class="abs" style="left:280px;top:44px;width:296px;text-align:center">Copyright @ 2011 www.velmorialimited.com</div>
  <div class="abs" style="left:290px;top:60px;width:276px;text-align:center;font-size:8.5px;line-height:12px">Sections 1.10.32 and 1.10.33 from "de Finibus Bonorum et Malorum" by<br>Aulus Fenwarin are also reproduced in their exact original form, accompanied by<br>English versions from the 1914 translation by H. Penmore.</div>
  <span class="vsep" style="left:604px"></span>
  <span class="abs" style="left:645px;top:19px">Follow us on :</span>
  <span class="social" style="left:705px;top:10px;background:#3b5c9a"></span>
  <span class="social" style="left:737px;top:10px;background:#3fb0e4"></span>
  <span class="social" style="left:769px;top:10px;background:#1d7bb0"></span>
  <span class="abs" style="left:645px;top:55px">Subscribe :</span>
  <span class="social" style="left:700px;top:46px;background:#f07d1a"></span>
</footer>

</body>
</html>
```